Psychotherapist need a business card with logo

I am a psychotherapist in need of a business card. The card must have:

Moravia Telvundor
Psicoterapeuta
937 218 604

Psychologists use the greek letter psy, which is the psychologist symbol, but I would prefer something like a mandala, a graphic symbol, an iconic tree, nothing very usual, but something that shows confidence and trust.

Industry/Entity Type

Business

```html
<!DOCTYPE html>
<html lang="es">
<head>
<meta charset="utf-8">
<title>Moravia Telvundor — Psicoterapeuta</title>
<link rel="stylesheet" href="https://fonts.googleapis.com/css2?family=Open+Sans:wght@400;700&display=swap">
<style>
  :root {
    --backdrop: #e6e6e6;
    --card-white: #fbfbfb;
    --band-black: #1c1c1c;
    --band-stripe: #262626;
    --ink-light: #ffffff;
    --ink-soft: #e4e4e4;
    --emblem-dark: #1a1a1a;
    --emblem-mid: #6a6a6a;
  }
  * { box-sizing: border-box; margin: 0; padding: 0; }
  html, body {
    width: 1200px;
    height: 800px;
    overflow: hidden;
    background: var(--backdrop);
    font-family: "Open Sans", Verdana, sans-serif;
  }
  .business-card {
    position: absolute;
    left: 110px;
    top: 120px;
    width: 980px;
    height: 560px;
    background: var(--card-white);
    box-shadow: 0 6px 18px rgba(0, 0, 0, 0.12);
    overflow: hidden;
  }
  .card-top {
    position: absolute;
    inset: 0 0 214px 0;
    background:
      repeating-linear-gradient(0deg, rgba(0,0,0,0.018) 0 1px, transparent 1px 3px),
      repeating-linear-gradient(90deg, rgba(0,0,0,0.018) 0 1px, transparent 1px 3px),
      var(--card-white);
  }
  .mandala-emblem {
    position: absolute;
    left: 50%;
    top: 173px;
    width: 284px;
    height: 284px;
    margin-left: -118px;
    margin-top: -142px;
    border-radius: 50%;
    background: radial-gradient(circle, var(--emblem-dark) 0 22%, var(--emblem-mid) 40%, var(--emblem-dark) 62%, #8a8a8a 80%, rgba(0,0,0,0) 100%);
  }
  .info-band {
    position: absolute;
    left: 0;
    right: 0;
    bottom: 0;
    height: 214px;
    background:
      repeating-linear-gradient(135deg, var(--band-stripe) 0 2px, var(--band-black) 2px 9px);
    color: var(--ink-light);
  }
  .practitioner {
    position: absolute;
    left: 61px;
    top: 58px;
  }
  .practitioner-name {
    font-size: 31px;
    font-weight: 700;
    line-height: 1.2;
  }
  .practitioner-role {
    font-size: 27px;
    font-weight: 400;
    line-height: 1.15;
    color: var(--ink-soft);
  }
  .contact-phone {
    position: absolute;
    right: 12px;
    top: 92px;
    font-size: 28px;
    font-weight: 400;
  }
  .contact-phone .label { font-weight: 700; }
</style>
</head>
<body>
  <article class="business-card">
    <section class="card-top">
      <div class="mandala-emblem" role="img" aria-label="Black and white circular mandala emblem with petal rings"></div>
    </section>
    <section class="info-band">
      <div class="practitioner">
        <p class="practitioner-name">Moravia Telvundor</p>
        <p class="practitioner-role">Psicoterapeuta</p>
      </div>
      <p class="contact-phone"><span class="label">Tel:</span> 937 218 604</p>
    </section>
  </article>
</body>
</html>
```